Design a business card & stationary for a mortgage company

We are looking for a good looking business card design for our mortgage company that includes our logo. We received a free design as part of our logo project but we don't love it. The company is called "Pinecrest Mortgage Company" so we like waves and lighthouses. The logo should be included. We have a version in both vertical and horizontal that we have provided.

Industry/Entity Type

Finance

Contact Information for Business Card

This should include our new logo file

Requirements
Must have
• 3. The details you'd like on the card - name, title, phone, email, website, address, social media handles etc.
1. Marcus Hale
Vice President
732-419-6253
Fax 888-304-2918
mhale@pinecrestmortgage.example
NMLS 47162 - Company NMLS 61290
18 Larkin Ave
Toms River, NJ 08614

```html
<!DOCTYPE html>
<html lang="en">
<head>
<meta charset="utf-8">
<title>Pinecrest Mortgage Company – Business Card</title>
<link href="https://fonts.googleapis.com/css2?family=Roboto:wght@400;700&display=swap" rel="stylesheet">
<style>
  :root {
    --backdrop: #1f2023;
    --brand-blue: #155a96;
    --brand-navy: #1a4a8a;
    --accent-blue: #2f8ad8;
    --paper: #ffffff;
    --ink-grey: #555a60;
    --rule: #4a7fb8;
  }
  * { margin: 0; padding: 0; box-sizing: border-box; }
  html, body {
    width: 1200px; height: 786px; overflow: hidden;
    background: var(--backdrop);
    font-family: "Roboto", Arial, sans-serif;
  }
  .canvas {
    position: relative; width: 1200px; height: 786px;
    display: flex; align-items: center; justify-content: center; gap: 40px;
  }
  .card {
    position: relative; width: 540px; height: 309px;
    box-shadow: 0 14px 30px rgba(0,0,0,.45);
  }
  /* Front */
  .card-front {
    background: var(--brand-blue);
    display: flex; align-items: center; justify-content: center; gap: 16px;
  }
  .brand-dot {
    width: 26px; height: 26px; border-radius: 50%;
    background: var(--paper); flex: none;
  }
  .brand-name-front {
    color: var(--paper); font-weight: 700; font-size: 26px;
    line-height: 1.15; letter-spacing: .5px;
  }
  /* Back */
  .card-back {
    background: var(--paper);
    display: flex; align-items: center;
    padding: 0 30px 0 40px;
  }
  .brand-block {
    width: 190px; display: flex; align-items: center; gap: 10px;
  }
  .brand-dot-small {
    width: 16px; height: 16px; border-radius: 50%;
    background: var(--brand-navy); flex: none;
  }
  .brand-name-back {
    color: var(--brand-navy); font-weight: 700; font-size: 17px; line-height: 1.2;
  }
  .divider {
    width: 1px; height: 150px; background: var(--rule);
    margin: 0 22px 0 14px; flex: none;
  }
  .contact { color: var(--ink-grey); font-size: 11.5px; line-height: 1.55; }
  .person-name { color: var(--brand-navy); font-weight: 700; font-size: 19px; line-height: 1.1; }
  .person-title { color: var(--accent-blue); font-weight: 700; font-size: 12.5px; margin-bottom: 10px; }
  .contact-row { display: flex; align-items: center; gap: 6px; }
  .contact-row svg { width: 11px; height: 11px; flex: none; fill: var(--accent-blue); }
</style>
</head>
<body>
<main class="canvas">
  <section class="card card-front">
    <span class="brand-dot"></span>
    <span class="brand-name-front">Pinecrest<br>Mortgage Company</span>
  </section>

  <section class="card card-back">
    <div class="brand-block">
      <span class="brand-dot-small"></span>
      <span class="brand-name-back">Pinecrest<br>Mortgage Company</span>
    </div>
    <div class="divider"></div>
    <div class="contact">
      <div class="person-name">Marcus Hale</div>
      <div class="person-title">Vice President</div>
      <div>NMLS 47162 - Company NMLS 61290</div>
      <div>18 Larkin Ave Toms River, NJ 08614</div>
      <div class="contact-row">
        <svg viewBox="0 0 12 12" aria-hidden="true"><path d="M2.5 1h2l1 3-1.3 1a7 7 0 0 0 2.8 2.8l1-1.3 3 1v2c0 .6-.4 1-1 1A9.5 9.5 0 0 1 1.5 2c0-.6.4-1 1-1z"/></svg>
        <span>732-419-6253</span>
      </div>
      <div class="contact-row">
        <svg viewBox="0 0 12 12" aria-hidden="true"><rect x="3" y="1" width="6" height="3"/><rect x="1" y="4.5" width="10" height="4.5" rx="1"/><rect x="3" y="8" width="6" height="3" fill="#fff" stroke="#2f8ad8"/></svg>
        <span>888-304-2918</span>
      </div>
      <div class="contact-row">
        <svg viewBox="0 0 12 12" aria-hidden="true"><rect x="1" y="2.5" width="10" height="7" rx="1"/><path d="M1.5 3l4.5 3.5L10.5 3" fill="none" stroke="#fff" stroke-width="1"/></svg>
        <span>mhale@pinecrestmortgage.example</span>
      </div>
      <div class="contact-row">
        <svg viewBox="0 0 12 12" aria-hidden="true"><circle cx="6" cy="6" r="5"/><path d="M1 6h10M6 1c-2.5 3-2.5 7 0 10M6 1c2.5 3 2.5 7 0 10" fill="none" stroke="#fff" stroke-width=".8"/></svg>
        <span>www.pinecrestmortgage.example</span>
      </div>
    </div>
  </section>
</main>
</body>
</html>
```